Social Media Template Design for a leading Veterinary Clinic in Austria

We are looking for social media design templates including the following:
- single picture posting (Snapvale & KL)
- carousel postings (Snapvale)
- story (Snapvale & KL)
- reel thumbnail (Snapvale & KL)
- story highlight design (Snapvale)

What are the templates for?
We are working on a way to make posting content more efficient. Therefore, we'd like to use templates for a more efficient content creation in the future. In this way on the one hand, we expect creating different kind of content to be easier and faster, on the other it should create consistency throughout our channels.. We work with Adobe CC and mostly use Photoshop or Indesign for content creation.

How should they look?
The two strongest colors of our CI are dark blue and gold. We expect templates in which these colors are the unifying element. We think that our logo does not have to appear. Our brand identity is modern, clean, professional, revolutionary and yet inviting. Our social presence should also convey this impression. Our postings contain images and text. As an example for template use, we plan on introducing our employees - here we would have to use the employee's photo and insert title and name.

At the moment it is hard to tell how many designs we will need in total, as we might need to adapt or extend the template after the first use cases.
But for the start we'd aprox. expect:
- 2-3 different story slides
- 3 carousel slides
- 1 reel thumbnail
- 1 story highlight design, in which we can adapt the icons on our own

Do you think, you can help us out?

Already looking forward to your design ideas! 😊 Feel free to contact us for any further questions.

Target Market(s)

Austria

Industry/Entity Type

Veterinary Medicine

Font styles to use
Serif
Sans Serif

Colors

Designer to choose colors to be used in the design.

Requirements
Must have
• templates for Adobe Photoshop or InDesign in formats 1:1, 9:16, 4:5 according to content (story, posting, reel etc.) and channel
Should not have
• ready-to-post content, content ideas - only templates we can fill with content

```html
<!DOCTYPE html>
<html lang="en">
<head>
<meta charset="utf-8">
<title>Tiervia – Social Media Templates</title>
<link href="https://fonts.googleapis.com/css2?family=Baloo+2:wght@700;800&family=Poppins:wght@400;800;900&display=swap" rel="stylesheet">
<style>
  :root {
    --bg: #c4dcdd;
    --navy: #243446;
    --gold: #c99a05;
    --white: #ffffff;
    --ink: #111111;
    --alert: #ff0000;
    --photo-a: #b9b6b0;
    --photo-b: #6f7378;
  }
  * { box-sizing: border-box; margin: 0; padding: 0; }
  html, body { width: 1200px; height: 1067px; overflow: hidden; }
  body { background: var(--bg); position: relative; font-family: "Poppins", sans-serif; }

  .note-banner {
    position: absolute; left: 0; top: 32px; width: 410px; height: 106px;
    background: var(--alert); color: var(--white);
    font-family: "Baloo 2", sans-serif; font-weight: 800; font-size: 32px; line-height: 44px;
    padding: 10px 0 0 84px; letter-spacing: 0.5px;
  }
  .section-label {
    position: absolute; font-family: "Baloo 2", sans-serif; font-weight: 800;
    font-size: 36px; color: var(--ink); white-space: nowrap; line-height: 1;
  }
  .guide-line { position: absolute; left: 84px; top: 176px; width: 1px; height: 713px; background: rgba(255,255,255,0.5); }

  .template { position: absolute; background: var(--navy); overflow: hidden; }
  .gold-band { position: absolute; left: 0; right: 0; bottom: 0; background: var(--gold); }

  .brand { position: absolute; display: flex; align-items: center; gap: 4px; }
  .brand--reverse { flex-direction: row-reverse; }
  .brand-dot { border-radius: 50%; background: var(--white); border: 2px solid var(--gold); flex: none; }
  .brand-name { font-family: "Poppins", sans-serif; font-weight: 800; color: var(--white); line-height: 1; }

  .headline { position: absolute; font-family: "Poppins", sans-serif; font-weight: 900; line-height: 0.92; text-transform: uppercase; }
  .headline span { display: block; }
  .headline .h-top { color: var(--white); }
  .headline .h-mid { color: var(--gold); }
  .headline .h-bot { color: var(--white); }
  .body-copy { position: absolute; color: var(--white); font-weight: 400; white-space: nowrap; }

  .photo-frame { position: absolute; border: 1.5px solid var(--white); border-radius: 26px; padding: 5px; }
  .photo { width: 100%; height: 100%; border-radius: 21px; background: linear-gradient(160deg, var(--photo-a), var(--photo-b)); }

  /* single post */
  .single-post { left: 657px; top: 32px; width: 288px; height: 288px; }
  .single-post .gold-band { height: 36px; }
  .single-post .photo-frame { left: 178px; top: 9px; width: 130px; height: 269px; }

  /* carousel */
  .carousel { left: 134px; top: 362px; width: 980px; height: 243px; }
  .carousel .gold-band { height: 30px; }
  .carousel .photo-frame { top: 9px; width: 188px; height: 225px; }
  .carousel .body-copy { top: 147px; font-size: 7.3px; line-height: 9.3px; }
  .carousel .body-copy--right { text-align: right; }

  /* story */
  .story { left: 116px; top: 644px; width: 225px; height: 401px; }
  .story .gold-band { height: 38px; }
  .story .photo-frame { left: 17px; top: 246px; width: 193px; height: 175px; }
</style>
</head>
<body>
  <div class="note-banner">PLEASE READ MY<br>COMMENTS</div>
  <div class="guide-line"></div>

  <div class="section-label" style="left:261px; top:146px;">single picture posting</div>
  <div class="section-label" style="left:645px; top:645px;">carousel&nbsp; Ads</div>
  <div class="section-label" style="left:371px; top:886px;">Story/reel thumbnail/story highlight</div>

  <!-- single post 1:1 -->
  <section class="template single-post">
    <div class="gold-band"></div>
    <div class="brand" style="left:13px; top:20px;">
      <span class="brand-dot" style="width:34px;height:34px;"></span>
      <span class="brand-name" style="font-size:9px;">Tiervia</span>
    </div>
    <h2 class="headline" style="left:23px; top:88px;">
      <span class="h-top" style="font-size:22px;">Heading</span>
      <span class="h-mid" style="font-size:35px;">Goes</span>
      <span class="h-bot" style="font-size:35px;">Here</span>
    </h2>
    <p class="body-copy" style="left:24px; top:173px; font-size:8.6px; line-height:11px;">Lorem ipsum dolor sit amet,<br>consectetur adipiscing elit,<br>sed do eiusmod tempor incid-</p>
    <div class="photo-frame"><div class="photo" role="img" aria-label="Photo of a vet nurse training a dog on a balance cushion"></div></div>
  </section>

  <!-- carousel 4 slides -->
  <section class="template carousel">
    <div class="gold-band"></div>

    <div class="photo-frame" style="left:151px;"><div class="photo" role="img" aria-label="Photo of two clinic team members with a kitten in the reception area"></div></div>
    <div class="photo-frame" style="left:641px;"><div class="photo" role="img" aria-label="Photo of two clinic team members each holding a kitten"></div></div>

    <div class="brand" style="left:21px; top:17px;"><span class="brand-dot" style="width:30px;height:30px;"></span><span class="brand-name" style="font-size:8px;">Tiervia</span></div>
    <div class="brand brand--reverse" style="right:511px; top:17px;"><span class="brand-dot" style="width:30px;height:30px;"></span><span class="brand-name" style="font-size:8px;">Tiervia</span></div>
    <div class="brand" style="left:511px; top:17px;"><span class="brand-dot" style="width:30px;height:30px;"></span><span class="brand-name" style="font-size:8px;">Tiervia</span></div>
    <div class="brand brand--reverse" style="right:21px; top:17px;"><span class="brand-dot" style="width:30px;height:30px;"></span><span class="brand-name" style="font-size:8px;">Tiervia</span></div>

    <h2 class="headline" style="left:20px; top:74px;"><span class="h-top" style="font-size:19px;">Heading</span><span class="h-mid" style="font-size:29px;">Goes</span><span class="h-bot" style="font-size:29px;">Here</span></h2>
    <p class="body-copy" style="left:20px;">Lorem ipsum dolor sit amet,<br>consectetur adipiscing elit,<br>sed do eiusmod tempor incid-</p>

    <h2 class="headline" style="left:384px; top:74px;"><span class="h-top" style="font-size:19px;">Heading</span><span class="h-mid" style="font-size:29px;">Goes</span><span class="h-bot" style="font-size:29px;">Here</span></h2>
    <p class="body-copy body-copy--right" style="right:511px;">Lorem ipsum dolor sit amet,<br>consectetur adipiscing elit,<br>sed do eiusmod tempor incid-</p>

    <h2 class="headline" style="left:510px; top:74px;"><span class="h-top" style="font-size:19px;">Heading</span><span class="h-mid" style="font-size:29px;">Goes</span><span class="h-bot" style="font-size:29px;">Here</span></h2>
    <p class="body-copy" style="left:510px;">Lorem ipsum dolor sit amet,<br>consectetur adipiscing elit,<br>sed do eiusmod tempor incid-</p>

    <h2 class="headline" style="left:873px; top:74px;"><span class="h-top" style="font-size:19px;">Heading</span><span class="h-mid" style="font-size:29px;">Goes</span><span class="h-bot" style="font-size:29px;">Here</span></h2>
    <p class="body-copy body-copy--right" style="right:21px;">Lorem ipsum dolor sit amet,<br>consectetur adipiscing elit,<br>sed do eiusmod tempor incid-</p>
  </section>

  <!-- story 9:16 -->
  <section class="template story">
    <div class="gold-band"></div>
    <div class="brand" style="left:92px; top:15px;">
      <span class="brand-dot" style="width:42px;height:42px;"></span>
    </div>
    <span class="brand-name" style="position:absolute; left:0; right:0; top:60px; text-align:center; font-size:8px;">Tiervia</span>
    <h2 class="headline" style="left:0; right:0; top:71px; text-align:center;">
      <span class="h-top" style="font-size:32px;">Heading</span>
      <span class="h-mid" style="font-size:49px;">Goes</span>
      <span class="h-bot" style="font-size:49px;">Here</span>
    </h2>
    <p class="body-copy" style="left:0; right:0; top:195px; font-size:12.5px; line-height:16px; text-align:center;">Lorem ipsum dolor sit amet,<br>consectetur adipiscing elit,</p>
    <div class="photo-frame"><div class="photo" role="img" aria-label="Photo of clinic team members in the reception area"></div></div>
  </section>
</body>
</html>
```